Bottom fuel dispenser panel

Design the fuel dispenser lower panel graphics based on our brand “vantora”
I will attach the brand logo and picture of the dispenser along with some other examples of other brands portraying their logos.

Target Market(s)

Petrol pump consumers

Industry/Entity Type

Oil and gas retailer

Requirements
Must have
• Theme that matches our brand
Nice to have
• Please refer to the image of the gas station in vantora branded photos. Size of the bottom panel is 28” by 45”.
Should not have
• Too many colors

```html
<!DOCTYPE html>
<html lang="en">
<head>
<meta charset="utf-8">
<title>vantora — dispenser lower panel</title>
<link rel="preconnect" href="https://fonts.googleapis.com">
<link href="https://fonts.googleapis.com/css2?family=Open+Sans:wght@800&display=swap" rel="stylesheet">
<style>
  :root {
    --brand-green: #99c93b;
    --brand-black: #000000;
    --panel-white: #ffffff;
    --page-bg: #ffffff;
    --panel-edge: #222222;
  }
  html, body {
    margin: 0;
    padding: 0;
    width: 1200px;
    height: 1200px;
    overflow: hidden;
    background: var(--page-bg);
  }
  .canvas {
    position: relative;
    width: 1200px;
    height: 1200px;
  }
  .dispenser-panel {
    position: absolute;
    left: 50px;
    top: 258px;
    width: 1100px;
    height: 684px;
    display: block;
  }
  .panel-ground { fill: var(--panel-white); stroke: var(--panel-edge); stroke-width: 1.2; }
  .sweep-green { fill: var(--brand-green); }
  .sweep-black { fill: var(--brand-black); }
  .brand-name {
    font-family: "Open Sans", Arial, sans-serif;
    font-weight: 800;
    font-size: 168px;
    letter-spacing: -6px;
    fill: var(--brand-black);
  }
</style>
</head>
<body>
  <main class="canvas">
    <svg class="dispenser-panel" viewBox="0 0 1062 660" xmlns="http://www.w3.org/2000/svg" aria-label="vantora fuel dispenser lower panel">
      <rect class="panel-ground" x="0.6" y="0.6" width="1060.8" height="658.8"/>
      <path class="sweep-green" d="M0,440 H640 Q860,440 1061,170 V300 Q890,530 660,530 H0 Z"/>
      <path class="sweep-black" d="M0,552 H680 Q910,552 1061,340 V390 Q930,590 690,590 H0 Z"/>
      <text class="brand-name" x="395" y="300" text-anchor="middle">vantora</text>
    </svg>
  </main>
</body>
</html>
```